La Brasa Dorada – CPG Website with WordPress - Store Locator: WP Maps plugin

Harlow Pantry Company is a startup consumer packaged goods (CPG) brand launching its flagship product line — La Brasa Dorada. We’re seeking a talented web designer to create a bold, professional, mobile-optimized website using WordPress with a WP Maps store locator to help customers find local retailers.

Our goal is to build a strong online presence that supports both retail growth and direct-to-consumer sales.

See La Brasa _Website_Design_Brief word document.

The website URL is https://labrasadorada.example/

Target Market(s)

Consumers of gourmet salsa

Industry/Entity Type

Consumer Packaged Goods - Salsa manufacturer.

Coding

Coded - Design and coding required

Number of Pages Required

5+ page

Requirements
Must have
• The design of the La Brasa Dorada website shall emulate the clean, polished aesthetic of Quillby.example.

```html
<!DOCTYPE html>
<html lang="en">
<head>
<meta charset="utf-8">
<title>La Brasa Dorada – Gourmet Salsa</title>
<link href="https://fonts.googleapis.com/css2?family=Poppins:wght@300;400;600;700;800&family=Bebas+Neue&display=swap" rel="stylesheet">
<style>
:root{
  --teal:#133b3b;
  --yellow:#efb536;
  --green:#8cab5d;
  --red:#c84526;
  --brown:#8a5a1f;
  --olive:#3f4f25;
  --label-yellow:#8a5a1f;
  --label-green:#4b5a2e;
  --label-red:#8a2a15;
  --text:#333;
  --white:#fff;
}
*{margin:0;padding:0;box-sizing:border-box}
html,body{width:1200px;height:3033px;overflow:hidden}
body{position:relative;font-family:'Poppins',sans-serif;color:var(--text);background:var(--white)}
.abs{position:absolute}

/* header */
.site-header{left:0;top:0;width:1200px;height:683px;background:var(--teal)}
.brand{left:100px;top:26px;font-weight:700;font-size:30px;color:var(--red);line-height:48px}
.main-nav{left:330px;top:40px;display:flex;gap:22px;font-weight:700;font-size:16px;color:var(--white);letter-spacing:.2px}
.main-nav .caret{font-size:10px;color:var(--yellow);margin-left:3px}
.header-icons{left:1043px;top:38px;display:flex;gap:14px}

/* hero */
.hero{left:25px;top:108px;width:1150px;height:550px;border-radius:24px;overflow:hidden;display:flex}
.hero-col{position:relative;height:100%}
.hero-col.natural{width:377px;background:var(--yellow)}
.hero-col.verde{width:395px;background:var(--green)}
.hero-col.habanero{flex:1;background:var(--red)}
.product-photo{position:absolute;left:50%;top:80px;width:240px;height:330px;margin-left:-120px;border-radius:14px}
.natural .product-photo{background:linear-gradient(180deg,#f3c257,#e88a33)}
.verde .product-photo{background:linear-gradient(180deg,#a3c06c,#7fa447)}
.habanero .product-photo{background:linear-gradient(180deg,#d95a36,#c33a22)}
.hero-label{position:absolute;left:0;right:0;top:452px;text-align:center;font-family:'Bebas Neue',sans-serif;font-size:46px;letter-spacing:1px}
.natural .hero-label{color:var(--label-yellow)}
.verde .hero-label{color:var(--label-green)}
.habanero .hero-label{color:var(--label-red)}

/* section titles */
.section-title{left:0;width:1200px;text-align:center;font-weight:700;font-size:40px;line-height:48px}
.rule{left:100px;width:1000px;height:1px}
.rule-bar{height:5px}

/* featured */
.featured-title{top:723px;color:var(--red)}
.featured-rule{top:780px;background:#e7a595}
.featured-bar{left:386px;width:427px;top:776px;background:var(--red)}
.featured-photo{left:124px;top:835px;width:372px;height:270px;border-radius:16px;background:linear-gradient(90deg,#e06a45,#a9c474 50%,#f1b04f)}
.featured-heading{left:558px;top:830px;font-weight:700;font-size:28px}
.featured-heading .h{color:var(--red)}
.featured-heading .v{color:var(--green)}
.featured-heading .n{color:#e89a25}
.featured-heading .c{color:#333}
.featured-copy{left:558px;top:890px;width:542px;font-size:14px;font-weight:300;line-height:20px;text-align:justify}
.btn{display:flex;align-items:center;justify-content:center;font-weight:700;font-size:16px;color:var(--white)}
.btn-shop{left:558px;top:1024px;width:209px;height:50px;background:var(--red)}

/* reviews */
.reviews{left:0;top:1154px;width:1200px;height:542px;background:var(--yellow)}
.reviews-title{top:1196px;color:var(--brown)}
.reviews-rule{top:1252px;background:#c8902a}
.reviews-bar{left:506px;width:190px;top:1247px;background:var(--brown)}
.review-card{top:1278px;width:291px;height:292px;background:var(--white);border-radius:12px;padding:22px 25px}
.quote-mark{font-family:'Bebas Neue',sans-serif;font-size:70px;line-height:48px;color:var(--brown);height:40px}
.review-head{font-weight:700;font-size:17px;line-height:25px;color:#222;margin-top:8px;height:54px}
.review-body{font-size:12px;font-weight:300;line-height:17.5px;text-align:justify;margin-top:6px;height:70px;overflow:hidden}
.stars{position:absolute;left:25px;top:218px;display:flex;gap:6px}
.arrow{width:42px;height:42px;border-radius:50%;display:flex;align-items:center;justify-content:center}
.arrow-brown{background:var(--brown)}
.arrow-olive{background:var(--olive)}
.btn-reviews{left:496px;top:1596px;width:208px;height:49px;background:var(--brown)}

/* recipes */
.recipes{left:0;top:1696px;width:1200px;height:812px;background:var(--green)}
.recipes-title{top:1736px;color:var(--olive)}
.recipes-rule{top:1791px;background:#6d8a43}
.recipes-bar{left:507px;width:186px;top:1786px;background:var(--olive)}
.recipe-card{left:100px;top:1817px;width:1000px;height:567px;background:var(--white);border-radius:26px}
.recipe-photo{left:184px;top:1858px;width:372px;height:483px;border-radius:22px;background:radial-gradient(circle at 55% 60%,#d27a2e,#a8461f 60%,#6d3a22)}
.recipe-heading{left:597px;top:1875px;font-weight:700;font-size:27px;color:var(--green)}
.recipe-copy{left:597px;top:1937px;width:420px;font-size:13.5px;font-weight:300;line-height:20px;text-align:justify}
.recipe-copy p+p{margin-top:20px}
.btn-recipe{left:597px;top:2229px;width:208px;height:50px;background:var(--olive)}
.btn-recipes{left:496px;top:2410px;width:208px;height:49px;background:var(--olive)}

/* social band */
.social-band{left:0;top:2508px;width:1200px;height:255px;background:var(--red)}
.social-mark{left:548px;top:2570px;width:104px;height:104px;border:9px solid var(--white);border-radius:50%}
.social-heading{left:0;width:1200px;top:2682px;text-align:center;font-weight:700;font-size:32px;color:var(--white)}

/* footer */
.footer-brand{left:100px;top:2830px;font-weight:700;font-size:54px;color:var(--red)}
.footer-col{top:2790px;text-align:center;font-weight:700;font-size:16px;line-height:32.4px;color:#222}
.footer-col.pages{left:413px;width:200px}
.footer-col.legal{left:669px;width:240px}
.footer-col.follow{left:982px;width:140px}
.follow-icons{display:flex;gap:9px;justify-content:center;margin-top:4px}
.follow-icons span{width:25px;height:25px;border-radius:4px;background:#e0902b}
.copyright{left:0;top:2971px;width:1200px;height:62px;background:var(--teal);color:var(--white);font-weight:700;font-size:17px;display:flex;align-items:center;justify-content:center}
</style>
</head>
<body>

<header class="site-header abs"></header>
<div class="brand abs">La Brasa</div>
<nav class="main-nav abs">
  <span>HOME</span><span>SHOP<span class="caret">▾</span></span><span>ABOUT US</span><span>WHERE TO BUY</span><span>RECIPES</span><span>CONTACT US</span>
</nav>
<div class="header-icons abs">
  <svg width="22" height="22" viewBox="0 0 22 22" fill="none" stroke="#fff" stroke-width="1.6"><circle cx="11" cy="7" r="4.5"/><path d="M3 21c0-4.5 3.6-7.5 8-7.5s8 3 8 7.5"/></svg>
  <svg width="24" height="22" viewBox="0 0 24 22" fill="none" stroke="#fff" stroke-width="1.6"><path d="M1 2h4l3 12h12l2.5-9H6.5"/><circle cx="10" cy="19" r="1.6"/><circle cx="18" cy="19" r="1.6"/></svg>
</div>

<section class="hero abs">
  <div class="hero-col natural"><div class="product-photo" role="img" aria-label="Product photo: All Natural salsa jar"></div><div class="hero-label">All Natural</div></div>
  <div class="hero-col verde"><div class="product-photo" role="img" aria-label="Product photo: Verde salsa jar"></div><div class="hero-label">Verde</div></div>
  <div class="hero-col habanero"><div class="product-photo" role="img" aria-label="Product photo: Habanero salsa jar"></div><div class="hero-label">Habanero</div></div>
</section>

<h2 class="section-title featured-title abs">FEATURED PRODUCT</h2>
<div class="rule featured-rule abs"></div>
<div class="rule-bar featured-bar abs"></div>
<div class="featured-photo abs" role="img" aria-label="Product photo: Habanero, Verde and All Natural salsa jars"></div>
<h3 class="featured-heading abs"><span class="h">Habanero</span><span class="c">, </span><span class="v">Verde</span><span class="c">, </span><span class="n">All Natural</span></h3>
<p class="featured-copy abs">Lorem Ipsum is simply dummy text of the printing and typesetting industry. Lorem Ipsum has been the industry's standard dummy text ever since the 1500s, when an unknown printer took a galley of type and scrambled it to make a type specimen book. It has survived not only five centuries, but also the leap into electronic typesetting, remaining essentially unchanged.</p>
<div class="btn btn-shop abs">SHOP NOW</div>

<section class="reviews abs"></section>
<h2 class="section-title reviews-title abs">REVIEWS</h2>
<div class="rule reviews-rule abs"></div>
<div class="rule-bar reviews-bar abs"></div>
<div class="arrow arrow-brown abs" style="left:71px;top:1403px"><svg width="14" height="14" viewBox="0 0 14 14"><path d="M9 2L4 7l5 5" fill="none" stroke="#fff" stroke-width="2"/></svg></div>
<div class="arrow arrow-brown abs" style="left:1087px;top:1403px"><svg width="14" height="14" viewBox="0 0 14 14"><path d="M5 2l5 5-5 5" fill="none" stroke="#fff" stroke-width="2"/></svg></div>

<article class="review-card abs" style="left:138px">
  <div class="quote-mark">“</div>
  <div class="review-head">“Very good, and I’m a salsa snob!”</div>
  <p class="review-body">Lorem Ipsum is simply dummy text of the printing and typesetting industry. Lorem Ipsum has been the industry's standard dummy text ever since the 1500s...</p>
  <div class="stars"><svg width="160" height="26" viewBox="0 0 160 26" fill="#efb536"><defs><path id="s1" d="M13 1l3.5 8 8.5.7-6.5 5.6 2 8.5L13 19.3 5.5 23.8l2-8.5L1 9.7 9.5 9z"/></defs><use href="#s1"/><use href="#s1" x="32"/><use href="#s1" x="64"/><use href="#s1" x="96"/><use href="#s1" x="128"/></svg></div>
</article>
<article class="review-card abs" style="left:455px">
  <div class="quote-mark">“</div>
  <div class="review-head">“Awesome taste, fresh.”</div>
  <p class="review-body">Lorem Ipsum is simply dummy text of the printing and typesetting industry. Lorem Ipsum has been the industry's standard dummy text ever since the 1500s...</p>
  <div class="stars"><svg width="160" height="26" viewBox="0 0 160 26" fill="#efb536"><use href="#s1"/><use href="#s1" x="32"/><use href="#s1" x="64"/><use href="#s1" x="96"/><use href="#s1" x="128"/></svg></div>
</article>
<article class="review-card abs" style="left:771px">
  <div class="quote-mark">“</div>
  <div class="review-head">“Really good flavor.”</div>
  <p class="review-body">Lorem Ipsum is simply dummy text of the printing and typesetting industry. Lorem Ipsum has been the industry's standard dummy text ever since the 1500s...</p>
  <div class="stars"><svg width="160" height="26" viewBox="0 0 160 26" fill="#efb536"><use href="#s1"/><use href="#s1" x="32"/><use href="#s1" x="64"/><use href="#s1" x="96"/><use href="#s1" x="128"/></svg></div>
</article>
<div class="btn btn-reviews abs">SHOW ALL REVIEWS</div>

<section class="recipes abs"></section>
<h2 class="section-title recipes-title abs">RECIPES</h2>
<div class="rule recipes-rule abs"></div>
<div class="rule-bar recipes-bar abs"></div>
<div class="recipe-card abs"></div>
<div class="recipe-photo abs" role="img" aria-label="Food photo: spoonful of beef and rice with melted cheese"></div>
<h3 class="recipe-heading abs">One Pot Mexican Beef and Rice</h3>
<div class="recipe-copy abs">
  <p>This One Pot Mexican Beef and Rice is the ultimate weeknight dinner—quick to prepare, easy to clean up, and packed with bold flavor in every bite. Ground beef is browned and simmered with beef broth, sweet corn, and La Brasa salsa, then combined with instant rice and melted cheddar for a hearty, satisfying meal that comes together in just 30 minutes.</p>
  <p>The star of the dish is La Brasa salsa, which infuses the beef and rice with a perfect balance of heat, brightness, and depth. Whether you use the All Natural, Habanero, or Verde variety, the salsa brings real flavor without the need for extra chopping or seasoning. It’s a one-pan recipe that’s both convenient and crave-worthy.</p>
</div>
<div class="btn btn-recipe abs">VIEW RECIPE</div>
<div class="arrow arrow-olive abs" style="left:32px;top:2079px"><svg width="14" height="14" viewBox="0 0 14 14"><path d="M9 2L4 7l5 5" fill="none" stroke="#fff" stroke-width="2"/></svg></div>
<div class="arrow arrow-olive abs" style="left:1124px;top:2079px"><svg width="14" height="14" viewBox="0 0 14 14"><path d="M5 2l5 5-5 5" fill="none" stroke="#fff" stroke-width="2"/></svg></div>
<div class="btn btn-recipes abs">SHOW ALL RECIPES</div>

<section class="social-band abs"></section>
<div class="social-mark abs"></div>
<h2 class="social-heading abs">FOLLOW LA BRASA DORADA ON PICTURA</h2>

<div class="footer-brand abs">La Brasa</div>
<div class="footer-col pages abs">SHOP<br>ABOUT US<br>WHERE TO BUY<br>RECIPES<br>CONTACT US</div>
<div class="footer-col legal abs">PRIVACY POLICY<br>SHIPPING POLICY<br>TERMS AND CONDITIONS</div>
<div class="footer-col follow abs">FOLLOW US<div class="follow-icons"><span></span><span></span><span></span></div></div>
<footer class="copyright abs">2025© All right reserved by La Brasa Dorada</footer>

</body>
</html>
```